Bright Lantern LLC Brochure

I am attaching a copy of my current brochure. To me it is plain and childish. I would like a brochure with color and pop! I will also attach some pictures from my courses feel free to crop and use. The language on the current brochure should stay somewhat the same in content. If you have better wording feel free to adjust it. I would just like the core content. My logo will also be attached.
Updates

Please incorporate "Health and Safety Educators" in the with the company name. Thank you much!

Font styles to use
Serif
Sans Serif

Colors

Designer to choose colors to be used in the design.

Requirements
Must have
• color and pop, must have my name Bright Lantern LLC, tag line "Learn It, Live It" content to draw parties to the brochure

```html
<!DOCTYPE html>
<html lang="en">
<head>
<meta charset="utf-8">
<title>Bright Lantern LLC Brochure</title>
<link rel="stylesheet" href="https://fonts.googleapis.com/css2?family=Libre+Baskerville:wght@400;700&family=Open+Sans:wght@400;600;700&display=swap">
<style>
:root{
  --red:#c41f2e;
  --red-dark:#8e1320;
  --charcoal:#3b3b3d;
  --paper:#ffffff;
  --ink:#333333;
  --muted:#6b6b6b;
  --stage:#e8e8e8;
  --serif:"Libre Baskerville", Georgia, serif;
  --sans:"Open Sans", Arial, sans-serif;
}
*{box-sizing:border-box;margin:0;padding:0}
html,body{width:1200px;height:2400px;overflow:hidden;background:var(--stage);font-family:var(--sans);color:var(--ink)}
.spread{position:absolute;left:40px;width:1120px;height:866px;display:flex;box-shadow:0 6px 24px rgba(0,0,0,.18);background:var(--paper)}
.spread--outside{top:190px}
.spread--inside{top:1300px}
.panel{position:relative;width:373.33px;height:100%;overflow:hidden}
.panel + .panel{border-left:1px solid rgba(0,0,0,.06)}
.photo{position:absolute;left:0;right:0}
.swoosh{position:absolute;left:0;width:100%;display:block}
.brand{font-family:var(--serif);color:var(--red);font-weight:700;white-space:nowrap}
.tagline{font-family:var(--serif);font-style:italic;color:var(--muted)}

/* outside: flap */
.flap .photo{top:0;height:300px;background:linear-gradient(160deg,#a98f7e,#5d6b7d 60%,#3f4a58)}
.flap__body{position:absolute;top:360px;left:34px;right:34px}
.flap__title{font-family:var(--serif);color:var(--red);font-size:26px;line-height:1.3;margin-bottom:18px}
.flap__text{font-size:16px;line-height:1.6;color:var(--ink)}
.flap__band{position:absolute;bottom:0;left:0;right:0;height:120px;background:var(--red);color:#fff;display:flex;align-items:center;justify-content:center;font-family:var(--serif);font-size:20px}

/* outside: back */
.back{background:var(--charcoal);color:#fff;text-align:center}
.back__mark{margin:90px auto 22px;width:120px;height:120px;border-radius:50%;background:var(--red)}
.back__name{font-family:var(--serif);font-size:26px;color:#fff;white-space:nowrap}
.back__tag{font-family:var(--serif);font-style:italic;font-size:15px;color:#d8d8d8;margin-top:8px}
.back__label{display:inline-block;margin-top:40px;background:var(--red);padding:8px 34px;font-weight:700;letter-spacing:2px;font-size:16px;text-transform:uppercase}
.back__list{list-style:none;margin-top:24px;font-size:16px;line-height:2}
.back__contact{position:absolute;bottom:60px;left:0;right:0;font-size:15px;line-height:1.9;color:#e6e6e6}
.back__contact .phone{display:inline-flex;gap:8px;align-items:center}

/* outside: cover */
.cover__head{position:absolute;top:60px;left:0;right:30px;text-align:right}
.cover__head .brand{font-size:27px}
.cover__head .tagline{font-size:16px;margin-top:8px}
.cover .photo{top:170px;height:420px;background:linear-gradient(150deg,#8ca0b3,#5a4f4a 55%,#2f3640)}
.cover__swoosh{top:540px;height:120px}
.cover__lead{position:absolute;top:660px;right:36px;left:36px;text-align:right;font-family:var(--serif);color:var(--red);font-size:24px;line-height:1.35}
.cover__band{position:absolute;bottom:0;left:0;right:0;height:60px;background:var(--red);color:#fff;font-size:14px;display:flex;align-items:center;justify-content:center}

/* inside: left */
.intro{background:var(--red);color:#fff}
.intro__body{position:absolute;top:56px;left:34px;right:34px}
.intro__title{font-family:var(--serif);font-size:30px;margin-bottom:20px}
.intro__text{font-size:16px;line-height:1.65;margin-bottom:18px}
.intro .photo{bottom:0;height:360px;background:linear-gradient(170deg,#5f8f8a,#2f5e6a 60%,#223d47)}
.intro__swoosh{bottom:300px;height:60px}

/* inside: middle */
.courses{text-align:center}
.courses__label{display:inline-block;margin-top:60px;background:var(--red);color:#fff;padding:8px 32px;font-weight:700;font-size:18px;letter-spacing:1px}
.icons{display:flex;justify-content:space-around;margin:44px 24px 0}
.icon{width:100px;font-size:14px;font-weight:600;color:var(--ink)}
.icon svg{display:block;margin:0 auto 10px}
.courses__name{font-size:29px;margin-top:70px}
.courses__tag{font-size:17px;margin-top:10px}
.courses__text{font-size:16px;line-height:1.6;margin:30px 40px 0;color:var(--ink)}
.courses__band{position:absolute;bottom:0;left:0;right:0;height:46px;background:var(--red)}

/* inside: right */
.why .photo{top:0;height:470px;background:linear-gradient(155deg,#7a6a63,#a88d86 40%,#4a4f5e)}
.why__swoosh{top:400px;height:71px}
.why__block{position:absolute;top:470px;bottom:0;left:0;right:0;background:var(--red);color:#fff;padding:50px 36px}
.why__title{font-family:var(--serif);font-size:28px;margin-bottom:18px}
.why__text{font-size:16px;line-height:1.65}
</style>
</head>
<body>

<section class="spread spread--outside" aria-label="Brochure outside">
  <div class="panel flap">
    <div class="photo" role="img" aria-label="Photo of a class group standing together in a training room"></div>
    <div class="flap__body">
      <h2 class="flap__title">Health and Safety Educators</h2>
      <p class="flap__text">Hands-on classes taught by certified instructors who care about your team.</p>
    </div>
    <div class="flap__band">Book your class today</div>
  </div>

  <div class="panel back">
    <div class="back__mark"></div>
    <div class="back__name">Bright Lantern LLC</div>
    <div class="back__tag">Learn It, Live It</div>
    <div class="back__label">Services</div>
    <ul class="back__list">
      <li>CPR and AED Training</li>
      <li>First Aid Certification</li>
      <li>Babysitter Safety Courses</li>
      <li>Group and Onsite Sessions</li>
    </ul>
    <div class="back__contact">
      <div class="phone"><svg width="16" height="16" viewBox="0 0 24 24"><path fill="#fff" d="M6.6 10.8a15 15 0 0 0 6.6 6.6l2.2-2.2c.3-.3.7-.4 1-.2 1.1.4 2.3.6 3.6.6.6 0 1 .4 1 1V20c0 .6-.4 1-1 1A17 17 0 0 1 3 4c0-.6.4-1 1-1h3.5c.6 0 1 .4 1 1 0 1.3.2 2.5.6 3.6.1.3 0 .7-.2 1z"/></svg>Call (555) 014-2290</div>
      <div>hello@brightlantern.example</div>
      <div>Serving schools, offices and homes</div>
    </div>
  </div>

  <div class="panel cover">
    <div class="cover__head">
      <div class="brand">Bright Lantern LLC</div>
      <div class="tagline">Learn It, Live It</div>
    </div>
    <div class="photo" role="img" aria-label="Photo of students practising CPR on training mannequins"></div>
    <svg class="swoosh cover__swoosh" viewBox="0 0 373 120" preserveAspectRatio="none" aria-hidden="true">
      <path d="M0 50 Q190 130 373 20 L373 120 L0 120Z" fill="#fff"/>
      <path d="M0 50 Q190 130 373 20 L373 38 Q190 140 0 68Z" fill="var(--red)"/>
    </svg>
    <p class="cover__lead">Providing health and safety needs for all environments</p>
    <div class="cover__band">Classes for every age and workplace</div>
  </div>
</section>

<section class="spread spread--inside" aria-label="Brochure inside">
  <div class="panel intro">
    <div class="intro__body">
      <h2 class="intro__title">Who We Are</h2>
      <p class="intro__text">Bright Lantern LLC teaches life saving skills in a relaxed, friendly setting where every student feels confident.</p>
      <p class="intro__text">Our courses meet current national guidelines and include a certification card.</p>
    </div>
    <div class="photo" role="img" aria-label="Photo of hands performing chest compressions on a mannequin"></div>
    <svg class="swoosh intro__swoosh" viewBox="0 0 373 60" preserveAspectRatio="none" aria-hidden="true">
      <path d="M0 0 L373 0 L373 20 Q180 70 0 40Z" fill="var(--red)"/>
    </svg>
  </div>

  <div class="panel courses">
    <div class="courses__label">CPR Classes</div>
    <div class="icons">
      <div class="icon"><svg width="64" height="64" viewBox="0 0 64 64"><circle cx="32" cy="32" r="30" fill="var(--red)"/><path d="M32 46 L18 32 a8 8 0 0 1 14-10 a8 8 0 0 1 14 10Z" fill="#fff"/></svg>Adult CPR</div>
      <div class="icon"><svg width="64" height="64" viewBox="0 0 64 64"><circle cx="32" cy="32" r="30" fill="var(--red)"/><path d="M27 16h10v11h11v10H37v11H27V37H16V27h11z" fill="#fff"/></svg>Child &amp; Infant</div>
      <div class="icon"><svg width="64" height="64" viewBox="0 0 64 64"><circle cx="32" cy="32" r="30" fill="var(--red)"/><path d="M19 33 l9 9 l17-19" stroke="#fff" stroke-width="6" fill="none" stroke-linecap="round" stroke-linejoin="round"/></svg>First Aid</div>
    </div>
    <div class="brand courses__name">Bright Lantern LLC</div>
    <div class="tagline courses__tag">Learn It, Live It</div>
    <p class="courses__text">Learn at your own pace with small groups and plenty of practice.</p>
    <div class="courses__band"></div>
  </div>

  <div class="panel why">
    <div class="photo" role="img" aria-label="Photo of a seated class group smiling during a course"></div>
    <svg class="swoosh why__swoosh" viewBox="0 0 373 71" preserveAspectRatio="none" aria-hidden="true">
      <path d="M0 30 Q200 90 373 10 L373 71 L0 71Z" fill="var(--red)"/>
    </svg>
    <div class="why__block">
      <h2 class="why__title">Why Choose Us</h2>
      <p class="why__text">Fun, interactive lessons and flexible scheduling for any group size.</p>
    </div>
  </div>
</section>

</body>
</html>
```